Garnett and Lyle Personal Injury Billboard

We'd like a clean/modern billboard to build brand awareness for our law firm in the area of personal injury. Ideally, we like the word "Injured?" or something similar in large lettering.

I'm attaching images, logo and award badges which could be used. The billboards will be 14x48 ft and 10.6x36.

We are open to different color ideas, fonts, and artwork. Creative but not too busy with wording. Our web page is www.kgarnettfirm.example

Garnett & Lyle Law Firm
(555) 318-4092

```html
<!DOCTYPE html>
<html lang="en">
<head>
<meta charset="utf-8">
<title>Garnett and Lyle Personal Injury Billboard</title>
<link rel="stylesheet" href="https://fonts.googleapis.com/css2?family=Montserrat:ital,wght@0,400;0,600;0,700;1,500;1,800&display=swap">
<style>
  :root {
    --navy: #1b3565;
    --navy-deep: #142a52;
    --sky: #1fa3e0;
    --white: #ffffff;
    --stage-dark: #333333;
    --stage-light: #6a9fd8;
    --backdrop: #eef0f3;
    --suit-light: #a3a7ae;
    --suit-mid: #7b8089;
    --suit-dark: #4f545d;
    --badge: #2f9fd9;
    --badge-edge: #12284e;
  }
  html, body {
    margin: 0;
    padding: 0;
    width: 847px;
    height: 1200px;
    overflow: hidden;
  }
  body {
    position: relative;
    font-family: "Montserrat", Arial, sans-serif;
    background: var(--stage-light);
  }
  .presentation-board {
    position: absolute;
    left: 0; top: 0;
    width: 847px; height: 565px;
    background: var(--stage-dark);
  }
  .billboard { position: absolute; display: block; }
  .billboard--wide { left: 106px; top: 107px; width: 635px; height: 184px; }
  .billboard--stacked { left: 152px; top: 313px; width: 540px; height: 194px; }
  .billboard--feature { left: 44px; top: 775px; width: 760px; height: 221px; }
  .headline { font-family: "Montserrat", Arial, sans-serif; fill: var(--navy); font-style: italic; }
  .headline-strong { font-weight: 800; }
  .headline-light { font-weight: 500; }
  .phone-number { font-family: "Montserrat", Arial, sans-serif; font-weight: 800; font-style: italic; fill: var(--white); }
  .firm-name { font-family: "Montserrat", Arial, sans-serif; font-weight: 700; }
  .firm-name--light { fill: var(--white); }
  .firm-name--dark { fill: var(--navy); }
</style>
</head>
<body>

<svg width="0" height="0" style="position:absolute" aria-hidden="true">
  <defs>
    <linearGradient id="portrait-backdrop" x1="0" y1="0" x2="1" y2="0">
      <stop offset="0" stop-color="var(--white)"/>
      <stop offset="0.75" stop-color="var(--backdrop)"/>
      <stop offset="1" stop-color="var(--navy)"/>
    </linearGradient>
    <linearGradient id="portrait-suits" x1="0" y1="0" x2="0" y2="1">
      <stop offset="0" stop-color="var(--suit-light)" stop-opacity="0"/>
      <stop offset="0.35" stop-color="var(--suit-light)" stop-opacity="0.55"/>
      <stop offset="0.6" stop-color="var(--suit-mid)"/>
      <stop offset="1" stop-color="var(--suit-dark)"/>
    </linearGradient>
    <radialGradient id="portrait-on-navy" cx="0.5" cy="0.75" r="0.7">
      <stop offset="0" stop-color="var(--suit-mid)"/>
      <stop offset="0.55" stop-color="var(--suit-dark)"/>
      <stop offset="1" stop-color="var(--navy)"/>
    </radialGradient>
    <linearGradient id="badge-tone" x1="0" y1="0" x2="0" y2="1">
      <stop offset="0" stop-color="var(--badge)"/>
      <stop offset="1" stop-color="#1b7fc0"/>
    </linearGradient>
    <symbol id="phone-icon" viewBox="0 0 24 24">
      <path d="M6.6 10.8a15.2 15.2 0 0 0 6.6 6.6l2.2-2.2a1 1 0 0 1 1-.25 11.4 11.4 0 0 0 3.6.57 1 1 0 0 1 1 1V20a1 1 0 0 1-1 1A17 17 0 0 1 3 4a1 1 0 0 1 1-1h3.5a1 1 0 0 1 1 1 11.4 11.4 0 0 0 .57 3.6 1 1 0 0 1-.25 1z" fill="#fff"/>
    </symbol>
    <symbol id="wide-design" viewBox="0 0 572 166">
      <rect x="0" y="0" width="572" height="166" fill="var(--white)"/>
      <rect x="283" y="0" width="289" height="166" fill="var(--navy)"/>
      <g role="img" aria-label="Photo of the two firm attorneys in grey suits">
        <rect x="283" y="0" width="180" height="166" fill="url(#portrait-backdrop)"/>
        <rect x="283" y="0" width="180" height="166" fill="url(#portrait-suits)"/>
      </g>
      <text class="headline" x="22" y="45" font-size="30"><tspan class="headline-strong">INJURED</tspan><tspan class="headline-light"> SOME</tspan></text>
      <text class="headline headline-strong" x="22" y="78" font-size="30">WHERE?</text>
      <polygon points="66,97 288,97 288,132 58,132" fill="var(--navy)"/>
      <circle cx="43" cy="115" r="21" fill="var(--sky)" stroke="var(--white)" stroke-width="2"/>
      <use href="#phone-icon" x="32" y="104" width="22" height="22"/>
      <text class="phone-number" x="78" y="122" font-size="19">(555) 318-4092</text>
      <text class="firm-name firm-name--light" x="458" y="30" font-size="12.5">GARNETT</text>
      <text class="firm-name firm-name--light" x="458" y="45" font-size="12.5">&amp; LYLE</text>
      <text class="firm-name firm-name--light" x="458" y="56" font-size="6.5">Law Firm PLLC</text>
      <rect x="477" y="81" width="40" height="53" rx="2" fill="url(#badge-tone)" stroke="var(--badge-edge)" stroke-width="1.5" role="img" aria-label="2023 choice award badge"/>
      <rect x="0.5" y="0.5" width="571" height="165" fill="none" stroke="var(--navy)" stroke-width="1"/>
    </symbol>
  </defs>
</svg>

<section class="presentation-board">
  <svg class="billboard billboard--wide" viewBox="0 0 572 166" role="img" aria-label="Garnett and Lyle wide billboard">
    <use href="#wide-design"/>
  </svg>

  <svg class="billboard billboard--stacked" viewBox="0 0 486 174" role="img" aria-label="Garnett and Lyle stacked billboard">
    <rect x="0" y="0" width="486" height="174" fill="var(--navy)"/>
    <rect x="280" y="6" width="206" height="168" fill="url(#portrait-on-navy)" role="img" aria-label="Photo of the two firm attorneys in grey suits"/>
    <polygon points="0,0 288,0 256,80 0,80" fill="var(--white)"/>
    <polygon points="0,108 250,108 224,174 0,174" fill="var(--white)"/>
    <text class="headline" x="18" y="35" font-size="27"><tspan class="headline-strong">INJURED</tspan><tspan class="headline-light"> SOME</tspan></text>
    <text class="headline headline-strong" x="18" y="66" font-size="27">WHERE?</text>
    <circle cx="40" cy="94" r="17" fill="var(--sky)" stroke="var(--white)" stroke-width="2"/>
    <use href="#phone-icon" x="31" y="85" width="18" height="18"/>
    <text class="phone-number" x="70" y="101" font-size="17">(555) 318-4092</text>
    <rect x="65" y="116" width="34" height="48" rx="2" fill="url(#badge-tone)" stroke="var(--badge-edge)" stroke-width="1.5" role="img" aria-label="2023 choice award badge"/>
    <text class="firm-name firm-name--dark" x="112" y="131" font-size="12">GARNETT</text>
    <text class="firm-name firm-name--dark" x="112" y="145" font-size="12">&amp; LYLE</text>
    <text class="firm-name firm-name--dark" x="112" y="156" font-size="6.5">Law Firm PLLC</text>
    <rect x="0.5" y="0.5" width="485" height="173" fill="none" stroke="var(--navy)" stroke-width="1"/>
  </svg>
</section>

<svg class="billboard billboard--feature" viewBox="0 0 572 166" role="img" aria-label="Garnett and Lyle roadside billboard">
  <use href="#wide-design"/>
</svg>

</body>
</html>
```